Nora Pettifer Music EP Design Artwork

EP musical recording cover art work. Nora Pettifer is a new artist in the Pop, Country Pop, Pop Rock, Americana and Singer-songwriter genres. The name of the EP is "Where the River Bends", and her first single is being released on all streaming platforms globally June 1st. We are looking for a graphic design that has that Pop/rock female artist appeal. norapettifer.net and all social media outlets are norapettifersongs (reference). Your art work will be seen globally and we will give a personal shout out on all her socials to the design we select as a single post. Her signature logo is attached for a color and style example. Please try to use the signature within the EP cover design, but feel free to change the purple backing accordingly if another color is needed to fit better with the color scheme of your design.

Requirements
Must have
• Nora Pettifer signature logo and EP name

Some of you asked for hi res pics, use this link:

https://files.quillbox.net/share/u/0/folders/8kTzW3pLqR2vN7xYcD4mHs1JbE6uAfGoQ
Should not have
• June 1 on the EP art work. June 1 is the release of the first single on the EP. This is an album cover, we want it to look like a really cool pop female artist album cover, thanks.

```html
<!DOCTYPE html>
<html lang="en">
<head>
<meta charset="utf-8">
<title>Nora Pettifer — Where the River Bends EP Cover</title>
<link rel="stylesheet" href="https://fonts.googleapis.com/css2?family=Raleway:wght@300;400&display=swap">
<style>
  :root {
    --stage: #9b9b9b;
    --brick: #b88878;
    --brick-deep: #8a5e52;
    --shade: #3a3034;
    --night: #1d1619;
    --denim: #3d5068;
    --ink-light: #ffffff;
  }
  html, body {
    margin: 0;
    padding: 0;
    width: 1200px;
    height: 900px;
    overflow: hidden;
    background: var(--stage);
  }
  .canvas {
    position: relative;
    width: 1200px;
    height: 900px;
  }
  .ep-cover {
    position: absolute;
    left: 190px;
    top: 40px;
    width: 820px;
    height: 820px;
    overflow: hidden;
    box-shadow: 0 18px 40px rgba(0, 0, 0, 0.28);
  }
  .cover-photo {
    position: absolute;
    inset: 0;
    background:
      linear-gradient(180deg, rgba(0,0,0,0) 55%, rgba(61,80,104,0.55) 100%),
      linear-gradient(95deg, var(--brick) 0%, var(--brick-deep) 28%, var(--shade) 55%, var(--night) 100%);
  }
  .ep-title {
    position: absolute;
    left: 50px;
    bottom: 28px;
    margin: 0;
    font-family: "Raleway", sans-serif;
    font-weight: 300;
    font-size: 50px;
    line-height: 1.08;
    letter-spacing: 0.5px;
    text-transform: uppercase;
    color: var(--ink-light);
  }
  .ep-title .title-line { display: block; }
  .ep-title .title-line--indent { padding-left: 96px; }
  .signature-line {
    position: absolute;
    right: 78px;
    top: 0;
    width: 3px;
    height: 120px;
    background: var(--ink-light);
    border-radius: 0 0 2px 2px;
  }
  .artist-name {
    position: absolute;
    right: 36px;
    bottom: 30px;
    margin: 0;
    writing-mode: vertical-rl;
    transform: rotate(180deg);
    font-family: "Raleway", sans-serif;
    font-weight: 400;
    font-size: 88px;
    line-height: 1;
    white-space: nowrap;
    color: var(--ink-light);
  }
</style>
</head>
<body>
  <main class="canvas">
    <section class="ep-cover">
      <div class="cover-photo" role="img" aria-label="Portrait photo of the smiling artist leaning on a café table in front of a brick wall"></div>
      <span class="signature-line" aria-hidden="true"></span>
      <h2 class="artist-name">Nora Pettifer</h2>
      <h1 class="ep-title">
        <span class="title-line">Where the</span>
        <span class="title-line title-line--indent">River Bends</span>
      </h1>
    </section>
  </main>
</body>
</html>
```